Design our letter, business card, powerpoint and more

We have a logo and want a design for our business use. Letters (word template), business card (for printing) powerpoint presentation (template) and more.

```html
<!DOCTYPE html>
<html lang="en">
<head>
<meta charset="utf-8">
<title>Norvale Business Card</title>
<link rel="stylesheet" href="https://fonts.googleapis.com/css2?family=Montserrat:wght@400;500;700&family=Open+Sans:wght@700&display=swap">
<style>
  :root {
    --page-bg: #e4e6ea;
    --card-white: #ffffff;
    --brand-blue: #8fa9d7;
    --brand-cyan: #7ccbe0;
    --brand-grey: #9c9698;
    --text-grey: #8a8587;
    --rule-grey: #c9c5c6;
  }
  * { box-sizing: border-box; margin: 0; padding: 0; }
  html, body { width: 1200px; height: 953px; overflow: hidden; }
  body {
    background: var(--page-bg);
    font-family: "Montserrat", sans-serif;
    position: relative;
  }
  .card {
    position: absolute;
    left: 290px;
    width: 620px;
    height: 354px;
    box-shadow: 0 3px 10px rgba(0,0,0,0.18);
    overflow: hidden;
  }
  .card-back { top: 70px; background: var(--brand-blue); }
  .card-front { top: 500px; background: var(--card-white); }

  .back-wordmark {
    position: absolute;
    inset: 0;
    display: flex;
    align-items: center;
    justify-content: center;
    font-family: "Open Sans", sans-serif;
    font-weight: 700;
    font-size: 84px;
    letter-spacing: 2px;
    color: var(--card-white);
  }

  .front-wordmark {
    position: absolute;
    left: 200px;
    top: 62px;
    display: flex;
    align-items: center;
    gap: 16px;
  }
  .wordmark-square {
    width: 40px; height: 40px;
    background: var(--brand-cyan);
  }
  .wordmark-text {
    font-family: "Open Sans", sans-serif;
    font-weight: 700;
    font-size: 60px;
    letter-spacing: 1px;
    color: var(--brand-grey);
    line-height: 1;
  }

  .person {
    position: absolute;
    right: 340px;
    top: 182px;
    text-align: right;
  }
  .person-name { font-size: 27px; line-height: 1; white-space: nowrap; }
  .person-first { color: var(--brand-cyan); font-weight: 400; }
  .person-last { color: var(--brand-blue); font-weight: 700; }
  .person-role { margin-top: 6px; font-size: 17px; color: var(--text-grey); }

  .divider {
    position: absolute;
    left: 298px; top: 178px;
    width: 1px; height: 84px;
    background: var(--rule-grey);
  }

  .contacts {
    position: absolute;
    left: 314px; top: 178px;
    list-style: none;
  }
  .contact-item {
    display: flex; align-items: center; gap: 9px;
    font-size: 17px; color: var(--text-grey);
    height: 28px;
  }
  .contact-icon { width: 16px; height: 16px; flex: none; }

  .address-band {
    position: absolute;
    left: 0; right: 0; top: 262px;
    height: 46px;
    background: var(--brand-blue);
    display: flex; align-items: center; justify-content: center;
    color: var(--card-white);
    font-size: 17px;
  }
</style>
</head>
<body>
  <section class="card card-back">
    <div class="back-wordmark">NORVALE</div>
  </section>

  <section class="card card-front">
    <div class="front-wordmark">
      <span class="wordmark-square"></span>
      <span class="wordmark-text">NORVALE</span>
    </div>

    <div class="person">
      <p class="person-name"><span class="person-first">MARA</span> <span class="person-last">LIND</span></p>
      <p class="person-role">Director / CEO</p>
    </div>

    <div class="divider"></div>

    <ul class="contacts">
      <li class="contact-item">
        <svg class="contact-icon" viewBox="0 0 16 16" aria-hidden="true"><path fill="#8fa9d7" d="M3.5 1.5l2.5 0 1 3.5-1.6 1.2c.8 1.8 2.2 3.2 4 4l1.2-1.6 3.5 1v2.5c0 .8-.7 1.5-1.5 1.4C6.9 13 3 9.1 2.1 3c-.1-.8.6-1.5 1.4-1.5z"/></svg>
        (555) 010-2468
      </li>
      <li class="contact-item">
        <svg class="contact-icon" viewBox="0 0 16 16" aria-hidden="true"><rect x="1" y="3" width="14" height="10" fill="#8fa9d7"/><path d="M1.5 3.5L8 9l6.5-5.5" fill="none" stroke="#fff" stroke-width="1.3"/></svg>
        info@norvale.com
      </li>
      <li class="contact-item">
        <svg class="contact-icon" viewBox="0 0 16 16" aria-hidden="true"><g fill="none" stroke="#8fa9d7" stroke-width="1.4"><circle cx="8" cy="8" r="6.5"/><ellipse cx="8" cy="8" rx="3" ry="6.5"/><path d="M1.5 8h13M2.5 4.8h11M2.5 11.2h11"/></g></svg>
        www.norvale.com
      </li>
    </ul>

    <div class="address-band">48 Harbor Row, Suite 210, Austin, TX 0000</div>
  </section>
</body>
</html>
```